Seabrook Botanics Facial Oil and Body Oil Packaging Project

We need a packaging concept for a Hemp based facial oil and body oil. We need label design for the bottle and carton graphics. I am attaching a few reference photos. The target demographic is women between 17-35 year old. Products need to be able to stand out in crowded stores with clear calls to action.
1oz Dropper Bottle with Unit Carton - Hemp Facial Oil
4oz PET Bottle with Unit Carton - Hemp + Rose Facial Oil

```html
<!DOCTYPE html>
<html lang="en">
<head>
<meta charset="utf-8">
<title>Seabrook Botanics – Facial Oil Packaging</title>
<link rel="stylesheet" href="https://fonts.googleapis.com/css2?family=Encode+Sans+Condensed:wght@400;500&family=Encode+Sans+Semi+Condensed:wght@400;500&family=Open+Sans:wght@400&display=swap">
<style>
  :root {
    --backdrop: #e4e4e4;
    --carton: #ffffff;
    --brand-green: #3f7a33;
    --ink-green: #1f4a1a;
    --label-green: #285c1f;
    --label-green-deep: #1d4716;
    --label-top: #eceeed;
    --leaf-light: #7bc142;
    --leaf-mid: #3f8f2a;
    --body-ink: #222222;
    --white: #ffffff;
  }
  * { box-sizing: border-box; margin: 0; padding: 0; }
  html, body { width: 1200px; height: 1200px; overflow: hidden; }
  body {
    background: linear-gradient(180deg, #f0f0f0 0%, var(--backdrop) 100%);
    position: relative;
    font-family: "Encode Sans Condensed", sans-serif;
  }
  .panel { position: absolute; background: var(--carton); box-shadow: 0 2px 10px rgba(0,0,0,.08); }

  /* Carton side panel */
  .carton-side { left: 90px; top: 150px; width: 230px; height: 900px; }
  .carton-side .brand {
    position: absolute; left: 24px; top: 90px; width: 182px;
    color: var(--brand-green); font-size: 34px; font-weight: 500; line-height: 1.05; text-align: center;
  }
  .carton-side .blurb {
    position: absolute; left: 20px; top: 330px; width: 190px;
    font-size: 13px; line-height: 2.1; text-align: center; color: var(--body-ink);
  }
  .carton-side .side-foot {
    position: absolute; left: 10px; right: 10px; top: 560px; bottom: 20px;
    background: linear-gradient(180deg, rgba(255,255,255,0) 0%, #dfe9d6 70%, #b7ca9f 100%);
    border-radius: 0 0 12px 12px;
  }
  .carton-side .leaf-art {
    position: absolute; left: 60px; top: 0; width: 130px; height: 290px;
    background: radial-gradient(ellipse at 60% 45%, var(--leaf-mid) 0%, rgba(63,143,42,.55) 45%, rgba(255,255,255,0) 72%);
  }
  .carton-side .side-name { position: absolute; left: 10px; bottom: 48px; font-size: 28px; color: var(--ink-green); }
  .carton-side .side-size { position: absolute; left: 10px; bottom: 16px; font-size: 20px; color: var(--ink-green); }

  /* Carton front panel */
  .carton-front { left: 340px; top: 150px; width: 400px; height: 900px; }
  .carton-front .brand {
    position: absolute; left: 20px; top: 110px; width: 360px;
    color: var(--brand-green); font-size: 58px; font-weight: 500; line-height: 1; text-align: center;
  }
  .carton-front .product {
    position: absolute; left: 0; top: 345px; width: 100%; text-align: center;
    font-family: "Encode Sans Semi Condensed", sans-serif; color: var(--ink-green);
  }
  .carton-front .product-name { font-size: 62px; font-weight: 400; line-height: 1; }
  .carton-front .product-sub { font-size: 40px; margin-top: 14px; color: #2b3a27; }
  .carton-front .leaf-art {
    position: absolute; left: 20px; top: 560px; width: 370px; height: 270px;
    background: radial-gradient(ellipse at 55% 55%, var(--leaf-light) 0%, var(--leaf-mid) 38%, rgba(63,143,42,.3) 62%, rgba(255,255,255,0) 78%);
  }
  .carton-front .size {
    position: absolute; left: 22px; bottom: 24px;
    font-family: "Open Sans", sans-serif; font-size: 30px; color: #1e1e1e;
  }

  /* Bottle label */
  .bottle-label { left: 770px; top: 380px; width: 340px; height: 400px; background: transparent; box-shadow: 0 2px 10px rgba(0,0,0,.08); }
  .bottle-label .label-top {
    position: absolute; left: 0; top: 0; width: 100%; height: 110px;
    background: linear-gradient(90deg, var(--white) 0%, var(--label-top) 100%);
  }
  .bottle-label .leaf-art {
    position: absolute; left: 10px; top: 15px; width: 110px; height: 80px;
    background: radial-gradient(ellipse at 50% 55%, var(--leaf-mid) 0%, rgba(123,193,66,.6) 45%, rgba(255,255,255,0) 72%);
  }
  .bottle-label .brand {
    position: absolute; left: 130px; top: 30px; width: 200px;
    color: var(--brand-green); font-size: 28px; font-weight: 500; line-height: 1.05;
  }
  .bottle-label .label-band {
    position: absolute; left: 0; top: 110px; width: 100%; height: 290px;
    background: linear-gradient(90deg, var(--label-green) 0%, var(--label-green-deep) 100%);
    font-family: "Open Sans", sans-serif; color: var(--white);
  }
  .bottle-label .label-name { position: absolute; left: 26px; top: 18px; font-size: 42px; line-height: 1.2; }
  .bottle-label .label-sub { position: absolute; left: 28px; top: 126px; font-size: 22px; }
  .bottle-label .label-size { position: absolute; left: 28px; bottom: 34px; font-size: 20px; }
  .bottle-label .drop { position: absolute; right: 30px; top: 40px; width: 110px; height: 180px; }
</style>
</head>
<body>

  <section class="panel carton-side">
    <div class="brand">Seabrook Botanics</div>
    <p class="blurb">Lorem Ipsum is simply dummy text of the printing and typesetting industry. Lorem Ipsum has been the industry's standard dummy text ever since the 1500s, when an unknown printer took a galley of type and scrambled it to make a type specimen book.</p>
    <div class="side-foot">
      <div class="leaf-art" role="img" aria-label="Hemp leaf photograph"></div>
      <div class="side-name">FACIAL OIL</div>
      <div class="side-size">1 oz 30 ml</div>
    </div>
  </section>

  <section class="panel carton-front">
    <div class="brand">Seabrook Botanics</div>
    <div class="product">
      <div class="product-name">FACIAL OIL</div>
      <div class="product-sub">with Hemp</div>
    </div>
    <div class="leaf-art" role="img" aria-label="Cluster of fresh hemp leaves photograph"></div>
    <div class="size">1 oz 30 ml</div>
  </section>

  <section class="panel bottle-label">
    <div class="label-top">
      <div class="leaf-art" role="img" aria-label="Hemp leaf photograph"></div>
      <div class="brand">Seabrook Botanics</div>
    </div>
    <div class="label-band">
      <div class="label-name">FACIAL<br>OIL</div>
      <div class="label-sub">with Hemp</div>
      <svg class="drop" viewBox="0 0 110 180" aria-hidden="true">
        <path d="M55 6 C55 60 6 90 6 130 A49 46 0 0 0 104 130 C104 90 55 60 55 6 Z" fill="none" stroke="#ffffff" stroke-width="2"/>
      </svg>
      <div class="label-size">1 oz 30 ml</div>
    </div>
  </section>

</body>
</html>
```